Business Card Design Project for - The Pellowick Greenworks Company Ltd. We are a Landscape and garden

I would like designer to use all special glosses etc so i can have a professional looking business card. The theme of the business card can reflect that of the Logo attached by MarkQuarry or your own unique ideas.. please feel free to go wild as i hope i can select a winner i like - my budget will be committed so please get involved. Good luck and thank you Lyndon

Target Market(s)

Must look Professional

General Public and Businesses including Councils, Local Government, Hospitals, Hotels, Professionals and Professional Sports People.

Industry/Entity Type

Landscape Gardening

Contact Information for Business Card

The Pellowick Greenworks Company Ltd

Mr L.R Ashcombe
Head Office - Quayfront Park Manchester
t. 0772 408 916
e. info@pellowickgreenworks.co.uk
w. www.pellowickgreenworks.co.uk

Facebook - https://www.friendpage-example.com/ThePellowickGreenworksCompany/
Twitter - https://chirpline-example.com/ThePruningCart
Instagram - https://www.snapgrid-example.com/thepellowickgreenworkscompany/?hl=en
Google+ - https://circles.searchhub-example.com/u/0/208473950162438571093
Yelp - https://www.reviewnook-example.co.uk/biz/the-pellowick-greenworks-company-manchester-4

Font styles to use
Serif
Script
Other font styles liked:
• I don't have much of an idea of font types sorry

Colors

Designer to choose colors to be used in the design.

Requirements
Must have
• A Professional look and Design
• Special effects with gloss and fading of colours possibly..
• Front and back design
Nice to have
• All special features with effects and gloss etc

```html
<!DOCTYPE html>
<html lang="en">
<head>
<meta charset="utf-8">
<title>The Pellowick Greenworks Company Ltd – Business Card</title>
<link rel="stylesheet" href="https://fonts.googleapis.com/css2?family=Cinzel:wght@400;700&family=Roboto+Condensed:wght@400;700&display=swap">
<style>
  :root {
    --backdrop: #5a5a5c;
    --card-black: #0c0c0d;
    --card-edge: #1e1e20;
    --leaf-green: #5fd13a;
    --leaf-deep: #2f9e27;
    --silver: #c9c9c9;
    --text-white: #f2f2f2;
    --muted-grey: #9a9a9a;
  }
  * { box-sizing: border-box; margin: 0; padding: 0; }
  html, body { width: 1200px; height: 852px; overflow: hidden; }
  body {
    background: var(--backdrop);
    position: relative;
    font-family: "Roboto Condensed", Arial, sans-serif;
  }
  .card {
    position: absolute;
    width: 520px;
    height: 300px;
    border-radius: 18px;
    background: linear-gradient(135deg, var(--card-edge) 0%, var(--card-black) 45%, #050505 100%);
    box-shadow: 0 14px 30px rgba(0,0,0,0.45);
    overflow: hidden;
  }
  .card::after {
    content: "";
    position: absolute;
    inset: 0;
    background: linear-gradient(115deg, transparent 30%, rgba(255,255,255,0.09) 42%, rgba(255,255,255,0.02) 55%, transparent 62%);
    pointer-events: none;
  }
  .card-front { left: 110px; top: 110px; }
  .card-back { left: 570px; top: 440px; }

  /* front */
  .front-brand {
    position: absolute;
    left: 0; right: 0; top: 92px;
    text-align: center;
  }
  .brand-dot {
    display: block;
    width: 46px; height: 46px;
    margin: 0 auto 14px;
    border-radius: 50%;
    background: radial-gradient(circle at 35% 35%, var(--leaf-green), var(--leaf-deep));
  }
  .front-name {
    font-family: "Cinzel", Georgia, serif;
    font-weight: 400;
    color: var(--silver);
    font-size: 27px;
    letter-spacing: 1px;
    line-height: 1.1;
  }
  .front-sub {
    font-family: "Cinzel", Georgia, serif;
    font-weight: 400;
    color: var(--silver);
    font-size: 11px;
    letter-spacing: 4px;
    margin-top: 6px;
  }

  /* back */
  .back-brand {
    position: absolute;
    left: 34px; top: 88px;
    width: 190px;
    text-align: center;
  }
  .back-brand .brand-dot { width: 70px; height: 70px; }
  .back-brand-name {
    font-family: "Cinzel", Georgia, serif;
    font-weight: 400;
    color: var(--leaf-green);
    font-size: 15px;
    line-height: 1.3;
  }
  .contact {
    position: absolute;
    left: 250px; top: 36px;
    color: var(--text-white);
  }
  .person-name {
    font-family: "Cinzel", Georgia, serif;
    font-weight: 700;
    color: var(--leaf-green);
    font-size: 19px;
    letter-spacing: 0.5px;
  }
  .person-office { font-size: 10.5px; font-weight: 700; margin-top: 2px; }
  .contact-list { list-style: none; margin-top: 12px; }
  .contact-list li {
    display: flex; align-items: center; gap: 8px;
    font-size: 11.5px; line-height: 17px;
  }
  .contact-icon { width: 12px; height: 12px; flex: none; }
  .social-list { list-style: none; margin-top: 10px; }
  .social-list li {
    display: flex; align-items: center; gap: 8px;
    font-size: 11px; line-height: 17px;
  }
  .social-dot {
    width: 11px; height: 11px; border-radius: 50%;
    background: var(--leaf-deep); flex: none;
  }
</style>
</head>
<body>

<section class="card card-front" aria-label="Business card front">
  <div class="front-brand">
    <span class="brand-dot"></span>
    <p class="front-name">THE PELLOWICK</p>
    <p class="front-sub">GREENWORKS COMPANY LTD</p>
  </div>
</section>

<section class="card card-back" aria-label="Business card back">
  <div class="back-brand">
    <span class="brand-dot"></span>
    <p class="back-brand-name">The Pellowick Greenworks Company Ltd</p>
  </div>

  <div class="contact">
    <p class="person-name">MR L.R ASHCOMBE</p>
    <p class="person-office">Head Office - Quayfront Park Manchester</p>

    <ul class="contact-list">
      <li>
        <svg class="contact-icon" viewBox="0 0 12 12"><rect x="0" y="0" width="12" height="12" rx="2" fill="var(--leaf-deep)"/><path d="M3 3.5c0 3 2.5 5.5 5.5 5.5l.8-1.3-1.6-.9-.8.8c-1-.4-1.8-1.2-2.2-2.2l.8-.8-.9-1.6z" fill="#fff"/></svg>
        0772 408 916
      </li>
      <li>
        <svg class="contact-icon" viewBox="0 0 12 12"><rect x="0" y="0" width="12" height="12" rx="2" fill="var(--leaf-deep)"/><rect x="2" y="3.5" width="8" height="5" fill="none" stroke="#fff" stroke-width="0.9"/><path d="M2 3.5l4 3 4-3" fill="none" stroke="#fff" stroke-width="0.9"/></svg>
        info@pellowickgreenworks.co.uk
      </li>
      <li>
        <svg class="contact-icon" viewBox="0 0 12 12"><circle cx="6" cy="6" r="6" fill="var(--leaf-deep)"/><circle cx="6" cy="6" r="3.6" fill="none" stroke="#fff" stroke-width="0.8"/><path d="M2.4 6h7.2M6 2.4c-1.6 2-1.6 5.2 0 7.2M6 2.4c1.6 2 1.6 5.2 0 7.2" fill="none" stroke="#fff" stroke-width="0.7"/></svg>
        www.pellowickgreenworks.co.uk
      </li>
    </ul>

    <ul class="social-list">
      <li><span class="social-dot"></span>ThePruningCart</li>
      <li><span class="social-dot"></span>thepellowickgreenworkscompany</li>
      <li><span class="social-dot"></span>208473950162438571093</li>
      <li><span class="social-dot"></span>ThePellowickGreenworksCompany</li>
      <li><span class="social-dot"></span>the-pellowick-greenworks-company-manchester</li>
    </ul>
  </div>
</section>

</body>
</html>
```